Healthy Supplement featuring Moringa products

Need 3 business card options for our reps to order from Cardloom. Our reps will be ordering from Cardloom once we upload them. Attached is our current designs to show what info needs to be on the cards. Our website is www.tkvitality.com
The business cards will be a template for our reps to order from. Most of our reps are Asian & Hispanic. Please look at our website so you can see who we are to get the look and feel what we need.
Target Market(s)
Adults 30 on up. Health oriented people.
Industry/Entity Type
Health And Wellness
Contact Information for Business Card
Name
Title
Phone
Logo
www.tkvitality.com/my/username
Font styles to use
Requirements
Must have
- Please match our website look and colors. A moringa leaf is nice, but am open to something different.
Nice to have
- Healthy looking and warm, not super cold or too modern.
Should not have
- No harsh colors please.

```html
<!DOCTYPE html>
<html lang="en">
<head>
<meta charset="utf-8">
<title>TK Vitality – Business Card</title>
<link href="https://fonts.googleapis.com/css2?family=Marcellus+SC&family=Open+Sans:wght@400;600&display=swap" rel="stylesheet">
<style>
  :root {
    --page-bg: #ecebe7;
    --card-dark: #3c3c3c;
    --card-dark-edge: #2f2f2f;
    --card-light: #ffffff;
    --card-light-shade: #ededed;
    --leaf-green: #8cc63f;
    --leaf-green-deep: #5fa83a;
    --faint-green: #e3ecda;
    --ink: #1e1e1e;
    --ink-soft: #333333;
  }
  * { box-sizing: border-box; margin: 0; padding: 0; }
  html, body {
    width: 1200px; height: 900px; overflow: hidden;
    background: var(--page-bg);
  }
  .canvas {
    position: relative; width: 1200px; height: 900px;
    display: flex; flex-direction: column; align-items: center; justify-content: center;
    gap: 56px;
  }
  .card {
    position: relative; width: 620px; height: 354px; overflow: hidden;
    box-shadow: 0 10px 26px rgba(0,0,0,0.18);
  }

  /* Back of card */
  .card-back {
    background: linear-gradient(135deg, var(--card-dark-edge) 0%, var(--card-dark) 45%, #4a4a4a 100%);
  }
  .brand-wordmark {
    position: absolute; left: 0; right: 0; top: 118px;
    text-align: center;
    font-family: "Marcellus SC", serif;
    font-size: 58px; letter-spacing: 4px;
    color: var(--leaf-green);
  }
  .brand-mark {
    display: inline-block; width: 22px; height: 22px; border-radius: 50%;
    background: var(--leaf-green); margin-right: 18px; vertical-align: 10px;
  }
  .url-band {
    position: absolute; left: 150px; top: 284px; width: 236px; height: 26px;
    background: var(--leaf-green-deep);
    border-radius: 0 13px 13px 0;
    font-family: "Marcellus SC", serif; font-size: 14px; letter-spacing: 2px;
    color: #2b3a1f; line-height: 26px; text-align: center;
  }
  .url-rule {
    position: absolute; left: 384px; right: 0; top: 296px; height: 3px;
    background: var(--leaf-green);
  }

  /* Front of card */
  .card-front {
    background: linear-gradient(120deg, var(--card-light) 0%, var(--card-light) 40%, var(--card-light-shade) 100%);
  }
  .watermark-disc {
    position: absolute; left: 200px; top: 70px; width: 230px; height: 230px;
    border-radius: 50%; background: var(--faint-green); opacity: 0.8;
  }
  .divider {
    position: absolute; left: 300px; top: 0; bottom: 0; width: 4px;
    background: var(--leaf-green);
  }
  .identity {
    position: absolute; right: 340px; top: 150px; text-align: right;
  }
  .person-name {
    font-family: "Marcellus SC", serif; font-size: 30px; color: var(--ink);
    letter-spacing: 1px; white-space: nowrap;
  }
  .person-title {
    font-family: "Open Sans", sans-serif; font-size: 18px; color: var(--leaf-green);
    margin-top: 2px;
  }
  .contact-list {
    position: absolute; left: 288px; top: 160px; list-style: none;
  }
  .contact-item {
    display: flex; align-items: center; height: 34px;
    font-family: "Open Sans", sans-serif; font-size: 18px; color: var(--ink-soft);
  }
  .contact-icon {
    width: 28px; height: 28px; border-radius: 50%;
    background: var(--leaf-green); margin-right: 22px;
    display: flex; align-items: center; justify-content: center;
    border: 3px solid var(--card-light);
  }
  .contact-icon svg { width: 14px; height: 14px; }
</style>
</head>
<body>
<main class="canvas">

  <section class="card card-back" aria-label="Card back">
    <div class="brand-wordmark"><span class="brand-mark"></span>TK Vitality</div>
    <div class="url-band">WWW.TKVITALITY.COM</div>
    <div class="url-rule"></div>
  </section>

  <section class="card card-front" aria-label="Card front">
    <div class="watermark-disc"></div>
    <div class="divider"></div>

    <div class="identity">
      <p class="person-name">Your Name</p>
      <p class="person-title">Job Title</p>
    </div>

    <ul class="contact-list">
      <li class="contact-item">
        <span class="contact-icon">
          <svg viewBox="0 0 24 24" fill="#fff"><path d="M6.6 10.8a15 15 0 0 0 6.6 6.6l2.2-2.2c.3-.3.7-.4 1-.2 1.1.4 2.3.6 3.6.6.6 0 1 .4 1 1V20c0 .6-.4 1-1 1A17 17 0 0 1 3 4c0-.6.4-1 1-1h3.5c.6 0 1 .4 1 1 0 1.3.2 2.5.6 3.6.1.3 0 .7-.2 1z"/></svg>
        </span>
        000 000 0000
      </li>
      <li class="contact-item">
        <span class="contact-icon">
          <svg viewBox="0 0 24 24" fill="none" stroke="#fff" stroke-width="2.4"><rect x="3" y="6" width="18" height="12" rx="1"/><path d="M3 7l9 6 9-6"/></svg>
        </span>
        youremail@xyz.com
      </li>
      <li class="contact-item">
        <span class="contact-icon">
          <svg viewBox="0 0 24 24" fill="none" stroke="#fff" stroke-width="2"><circle cx="12" cy="12" r="9"/><path d="M3 12h18M12 3c3 3 3 15 0 18M12 3c-3 3-3 15 0 18"/></svg>
        </span>
        www.tkvitality.com
      </li>
    </ul>
  </section>

</main>
</body>
</html>
```